Tidewell Recovery Business Card Design

Professional and clean design. The design colors should flow with the logo. Two-sided card with the website on the back which is:

www.TidewellRecovery.example.

"Specializing in Water Damage Restoration"

On the front I need the name, email, phone, and logo.

Name: Dorian Vashti
Email: Dorian@TidewellRecovery.example
Phone: 555-318-2046 for now

I only have the Preview and Thumbnail right now but should have the source files uploaded within a day or two.

Target Market(s)

Flood victims, home owners with water damage from busted pipes etc...

Industry/Entity Type

Business

Contact Information for Business Card

Name: Dorian Vashti

Font styles to use
Serif
Sans Serif

```html
<!DOCTYPE html>
<html lang="en">
<head>
<meta charset="utf-8">
<title>Tidewell Recovery Business Card</title>
<link rel="stylesheet" href="https://fonts.googleapis.com/css2?family=Cinzel:wght@600&family=Open+Sans:ital,wght@0,400;1,700&family=Jost:wght@400;500&display=swap">
<style>
  :root {
    --brand-blue: #2196d3;
    --brand-light: #5cc0ef;
    --paper: #ffffff;
    --backdrop: #e9ecef;
    --card-shadow: rgba(0, 0, 0, 0.18);
  }
  * { box-sizing: border-box; margin: 0; padding: 0; }
  html, body {
    width: 1200px;
    height: 1200px;
    overflow: hidden;
    background: var(--backdrop);
  }
  .canvas {
    position: relative;
    width: 1200px;
    height: 1200px;
  }
  .card {
    position: absolute;
    left: 150px;
    width: 900px;
    height: 514px;
    overflow: hidden;
    box-shadow: 0 10px 30px var(--card-shadow);
  }
  .card--back { top: 48px; background: var(--brand-blue); color: var(--paper); }
  .card--front { top: 622px; background: var(--paper); }

  .brand-mark {
    position: absolute;
    left: 50%;
    transform: translateX(-50%);
    width: 100px;
    height: 100px;
    border-radius: 50%;
  }
  .card--back .brand-mark { top: 56px; background: var(--paper); }
  .card--front .brand-mark { top: 40px; left: 480px; background: var(--brand-blue); }

  .brand-name {
    position: absolute;
    width: 100%;
    text-align: center;
    font-family: "Cinzel", serif;
    font-weight: 600;
    font-size: 40px;
    line-height: 1.2;
    letter-spacing: 2px;
    text-transform: uppercase;
  }
  .card--back .brand-name { top: 182px; color: var(--paper); }
  .card--front .brand-name { top: 162px; left: 30px; color: var(--brand-blue); }

  .tagline-row {
    position: absolute;
    top: 282px;
    left: 0;
    width: 100%;
    display: flex;
    align-items: center;
    gap: 22px;
  }
  .tagline-rule { flex: 1; height: 2px; background: var(--paper); }
  .tagline-rule--left { margin-top: 42px; }
  .tagline {
    font-family: "Open Sans", sans-serif;
    font-style: italic;
    font-weight: 700;
    font-size: 26px;
  }
  .website {
    position: absolute;
    top: 388px;
    width: 100%;
    text-align: center;
    font-family: "Jost", sans-serif;
    font-size: 24px;
  }

  .wave { position: absolute; inset: 0; width: 900px; height: 514px; }
  .wave-fill { fill: var(--brand-blue); }
  .wave-swoosh { fill: var(--brand-light); }

  .person {
    position: absolute;
    left: 92px;
    top: 390px;
    color: var(--paper);
    font-family: "Jost", sans-serif;
  }
  .person-name { font-size: 28px; font-weight: 500; }
  .person-role { font-size: 28px; font-weight: 400; margin-top: 4px; }

  .contact {
    position: absolute;
    left: 452px;
    top: 312px;
    list-style: none;
    color: var(--paper);
    font-family: "Jost", sans-serif;
    font-size: 24px;
  }
  .contact-item { display: flex; align-items: center; gap: 12px; height: 36px; }
  .contact-icon { width: 24px; height: 24px; fill: var(--paper); flex: none; }
</style>
</head>
<body>
<main class="canvas">

  <section class="card card--back" aria-label="Card back">
    <span class="brand-mark" aria-hidden="true"></span>
    <h2 class="brand-name">Tidewell Recovery</h2>
    <div class="tagline-row">
      <span class="tagline-rule tagline-rule--left"></span>
      <p class="tagline">Specializing in Water Damage Restoration</p>
      <span class="tagline-rule"></span>
    </div>
    <p class="website">www.TidewellRecovery.example</p>
  </section>

  <section class="card card--front" aria-label="Card front">
    <svg class="wave" viewBox="0 0 900 514" aria-hidden="true">
      <path class="wave-fill" d="M0,340 C350,290 760,300 900,80 L900,514 L0,514 Z"/>
      <path class="wave-swoosh" d="M0,300 C100,270 220,255 340,250 C220,265 100,290 0,322 Z"/>
    </svg>
    <span class="brand-mark" aria-hidden="true"></span>
    <h2 class="brand-name">Tidewell Recovery</h2>

    <div class="person">
      <p class="person-name">Dorian Vashti</p>
      <p class="person-role">CEO</p>
    </div>

    <ul class="contact">
      <li class="contact-item">
        <svg class="contact-icon" viewBox="0 0 24 24" aria-hidden="true">
          <path d="M2 5h20v14H2z M3.5 6.5 12 13l8.5-6.5" fill="none" stroke="#fff" stroke-width="2"/>
        </svg>
        Dorian@TidewellRecovery.example
      </li>
      <li class="contact-item">
        <svg class="contact-icon" viewBox="0 0 24 24" aria-hidden="true">
          <path d="M2 8c0-3 4-5 10-5s10 2 10 5v2h-5V8H7v2H2z M5 12h14l2 9H3z"/>
        </svg>
        555-318-2046
      </li>
    </ul>
  </section>

</main>
</body>
</html>
```